Creation of a construction/bricklaying business website

Following the template format of "Wendmoor 2", the following content would need to be included:
1. Landing page with 3 tiles that go to their own pages.
- Landing page to include background photo and description of services offered.
2. 3 tiles to include:
a) "Contact Us For A Free Quote or Friendly Discussion" Form (middle tile)
b) Case Studies and Testimonials
c) Certifications and Professional Membership
- Design logo to be used from previous PixelHarbor project. Example of logo attached below, please access full JPG files from our account.

Target Market(s)

Prospective clients seeking construction work (bricklaying speciality)

Industry/Entity Type

Residential Construction

Coding

Coded - Design and coding required

Number of Pages Required

4 page

Font styles to use
Sans Serif

Colors

Designer to choose colors to be used in the design.

Requirements
Must have
• Following the template format of "Wendmoor 2", the following content would need to be included:
• 1. Landing parent page with 3 tiles that go to the 3 child pages.
• - Landing page to include background photo and description of services offered.
• 2. 3 tiles to include:
• a) "Contact Us For A Free Quote or Friendly Discussion" Form (middle tile)
• b) Case Studies and Testimonials (first tile / left side)
• c) Certifications and Professional Memberships (third tile / right side) (This should include logos of the relevant organisations being displayed. Specifically QLT and the Keystone Pact QLT).
• - Design logo to be used from previous PixelHarbor project. Example of logo attached below, please access full JPG files from our account.
Nice to have
• Sleek and modern feel.
• Approachable in terms of how people can contact the company for a quote.
• Traditional pictures to give credibility and comfort around choosing this company.
Should not have
• Cheesy pictures
• Over-complicated
• Simple to use
• Easy URL domain name

```html
<!DOCTYPE html>
<html lang="en">
<head>
<meta charset="utf-8">
<title>R.T.Harlow Construction Ltd</title>
<link href="https://fonts.googleapis.com/css2?family=Varela+Round&family=Questrial&display=swap" rel="stylesheet">
<style>
  :root{
    --brand:#0d56a6;
    --brand-dark:#0a3f7c;
    --ink:#1d1d1d;
    --text:#222;
    --tile:#e8ecee;
    --white:#fff;
    --icon-bg:#eeeff1;
    --badge-red:#c8102e;
    --placeholder:#b9c3cc;
  }
  *{margin:0;padding:0;box-sizing:border-box}
  html,body{width:920px;height:1200px;overflow:hidden;background:var(--white)}
  body{position:relative;font-family:"Questrial",sans-serif;color:var(--text)}
  .hero{position:absolute;left:0;top:0;width:920px;height:315px;
    background:linear-gradient(160deg,#6d5a52 0%,#7a4a3c 30%,#5e3a30 55%,#6a6864 80%,#8a8a86 100%)}
  .hero::after{content:"";position:absolute;inset:0;background:rgba(0,0,0,.28)}
  .contact-item{position:absolute;z-index:2;display:flex;align-items:center;gap:8px;color:var(--white);font-size:11.5px;line-height:16px}
  .contact-item .badge{width:29px;height:29px;border-radius:50%;background:var(--brand);display:flex;align-items:center;justify-content:center;flex:none}
  .hero .call{left:124px;top:13px}
  .hero .mail{left:626px;top:13px}
  .brand-name{position:absolute;z-index:2;left:0;width:920px;top:140px;text-align:center;font-family:"Varela Round",sans-serif;color:var(--white);font-size:34px}
  .nav{position:absolute;left:0;top:315px;width:920px;height:36px;background:var(--brand);display:flex;align-items:center;padding-left:132px;gap:19px;font-family:"Varela Round",sans-serif;font-size:12.3px;color:var(--white)}
  .nav .current{color:var(--ink)}
  .nav span:last-child{margin-left:3px}
  .about-title{position:absolute;top:380px;width:920px;text-align:center;font-family:"Varela Round",sans-serif;font-weight:400;color:var(--brand);font-size:21px}
  .about-lead{position:absolute;top:422px;left:175px;width:570px;text-align:center;font-family:"Varela Round",sans-serif;font-size:14.2px;line-height:17.5px;color:var(--ink)}
  .service{position:absolute;top:482px;width:110px;margin-left:-55px;text-align:center}
  .service .ring{width:78px;height:78px;margin:0 auto;border-radius:50%;border:3px solid var(--brand);background:radial-gradient(circle at 50% 40%,#fff,var(--icon-bg));display:flex;align-items:center;justify-content:center;box-shadow:0 6px 5px -4px rgba(0,0,0,.18)}
  .service .label{margin-top:21px;font-family:"Varela Round",sans-serif;font-size:14.5px;line-height:17.5px;color:var(--ink)}
  .intro{position:absolute;top:644px;left:128px;width:664px;text-align:center;font-size:12.3px;line-height:18.5px;color:var(--ink)}
  .intro p+p{margin-top:12px}
  .tile{position:absolute;top:754px;width:224px;height:208px;text-align:center;padding:20px 6px 0}
  .tile.shaded{background:var(--tile)}
  .tile .icon{height:50px;display:flex;justify-content:center;align-items:flex-end}
  .tile .icon-placeholder{width:74px;height:48px;border-radius:4px;background:var(--placeholder)}
  .tile h3{margin-top:14px;font-family:"Varela Round",sans-serif;font-weight:400;font-size:10.8px;line-height:14.5px;color:var(--ink)}
  .tile p{margin-top:10px;font-size:10.2px;line-height:16.5px;color:var(--ink)}
  .tile a{display:block;margin-top:8px;font-family:"Varela Round",sans-serif;color:var(--brand);font-size:11px;text-decoration:none}
  .footer{position:absolute;left:0;top:1008px;width:920px;height:192px;background:linear-gradient(180deg,#6f6a62 0%,#5b5750 55%,#3f3d3a 100%)}
  .footer::after{content:"";position:absolute;inset:0;background:rgba(0,0,0,.38)}
  .footer-name{position:absolute;z-index:2;top:40px;width:920px;text-align:center;font-family:"Varela Round",sans-serif;color:var(--white);font-size:15px}
  .footer .addr{left:146px;top:86px}
  .footer .call{left:393px;top:86px}
  .footer .mail{left:597px;top:86px}
  .footer .contact-item{font-size:11px}
  .copyright{position:absolute;z-index:2;left:146px;top:169px;color:var(--white);font-size:11px}
  .social{position:absolute;z-index:2;left:662px;top:153px;display:flex;gap:4px}
  .social span{width:23px;height:23px;border-radius:50%;background:var(--white)}
</style>
</head>
<body>
  <header class="hero" role="img" aria-label="Photo of a newly built red brick garden wall in front of terraced houses, with building tools on the pavement">
    <div class="contact-item call">
      <span class="badge"><svg width="14" height="14" viewBox="0 0 24 24"><path fill="#fff" d="M6.6 10.8a15.1 15.1 0 0 0 6.6 6.6l2.2-2.2c.3-.3.7-.4 1-.2 1.1.4 2.3.6 3.6.6.6 0 1 .4 1 1V20c0 .6-.4 1-1 1C10.6 21 3 13.4 3 4c0-.6.4-1 1-1h3.5c.6 0 1 .4 1 1 0 1.3.2 2.5.6 3.6.1.3 0 .7-.2 1z"/></svg></span>
      <span>Call Us On<br>123.456.7890</span>
    </div>
    <div class="contact-item mail">
      <span class="badge"><svg width="15" height="12" viewBox="0 0 20 14"><rect x="1" y="1" width="18" height="12" fill="none" stroke="#fff" stroke-width="1.6"/><path d="M1 1l9 7 9-7" fill="none" stroke="#fff" stroke-width="1.6"/></svg></span>
      <span>Email Us On<br>info@rtharlowconstruction.com</span>
    </div>
    <div class="brand-name">R.T.Harlow Construction Ltd</div>
  </header>

  <nav class="nav">
    <span class="current">Home</span>
    <span>Case Studies &amp; Testimonials</span>
    <span>Contact Us For A Free Quote</span>
    <span>Certifications &amp; Professional Memberships</span>
  </nav>

  <h1 class="about-title">About Us</h1>
  <p class="about-lead">R.T.Harlow Construction Ltd is a construction company that has expertise and experience in the following areas</p>

  <div class="service" style="left:163px">
    <div class="ring"><svg width="40" height="36" viewBox="0 0 40 36"><path d="M6 16L20 5l14 11" fill="none" stroke="#333" stroke-width="2"/><rect x="10" y="15" width="20" height="14" fill="none" stroke="#333" stroke-width="2"/><rect x="14" y="19" width="5" height="5" fill="#333"/><rect x="22" y="19" width="4" height="10" fill="#333"/><path d="M4 33h32" stroke="#333" stroke-width="1.5"/></svg></div>
    <div class="label">Extensions</div>
  </div>
  <div class="service" style="left:281px">
    <div class="ring"><svg width="40" height="36" viewBox="0 0 40 36"><path d="M4 18L20 4l16 14" fill="none" stroke="#333" stroke-width="3"/><path d="M9 15v17h22V15" fill="none" stroke="#333" stroke-width="3"/><rect x="14" y="19" width="5" height="5" fill="#333"/><rect x="22" y="20" width="5" height="12" fill="#333"/><rect x="27" y="5" width="4" height="8" fill="#333"/></svg></div>
    <div class="label">New build /<br>New houses</div>
  </div>
  <div class="service" style="left:406px">
    <div class="ring"><svg width="46" height="32" viewBox="0 0 46 32"><g fill="#333"><rect x="2" y="2" width="26" height="3"/><rect x="2" y="8" width="13" height="5"/><rect x="17" y="8" width="13" height="5"/><rect x="32" y="8" width="12" height="5"/><rect x="2" y="15" width="6" height="5"/><rect x="10" y="15" width="13" height="5"/><rect x="25" y="15" width="13" height="5"/><rect x="40" y="15" width="4" height="5"/><rect x="2" y="22" width="13" height="5"/><rect x="17" y="22" width="13" height="5"/><rect x="32" y="22" width="12" height="5"/></g></svg></div>
    <div class="label">Garden walls</div>
  </div>
  <div class="service" style="left:518px">
    <div class="ring"><svg width="44" height="36" viewBox="0 0 44 36"><g fill="none" stroke="#333" stroke-width="1.8"><rect x="3" y="4" width="12" height="6"/><rect x="15" y="4" width="12" height="6"/><rect x="3" y="10" width="7" height="6"/><rect x="10" y="10" width="12" height="6"/><rect x="3" y="16" width="12" height="6"/><rect x="3" y="22" width="7" height="6"/><path d="M22 30l10-16 4 3-8 15z"/><path d="M34 15l6 12"/></g></svg></div>
    <div class="label">Plastering</div>
  </div>
  <div class="service" style="left:638px">
    <div class="ring"><svg width="44" height="36" viewBox="0 0 44 36"><g fill="#333"><path d="M6 3h3v10l3 5-4 6-4-6 2-5z"/><rect x="14" y="16" width="10" height="4"/><rect x="26" y="16" width="10" height="4"/><rect x="8" y="23" width="10" height="4"/><rect x="20" y="23" width="10" height="4"/><rect x="32" y="23" width="8" height="4"/><rect x="14" y="30" width="10" height="4"/><rect x="26" y="30" width="10" height="4"/></g></svg></div>
    <div class="label">Brickwork</div>
  </div>
  <div class="service" style="left:758px">
    <div class="ring"><svg width="44" height="38" viewBox="0 0 44 38"><g fill="#333"><rect x="6" y="2" width="10" height="3"/><rect x="10" y="5" width="2" height="16"/><path d="M5 21h12v10a6 6 0 0 1-12 0z"/><path d="M20 34l8-12 5 5 4-3 5 10z"/><circle cx="38" cy="22" r="2"/></g></svg></div>
    <div class="label">Groundworks</div>
  </div>

  <div class="intro">
    <p>We pride ourselves on attention to detail, pride in our completed project and client satisfaction. We believe in full transparency and this is reflected in the jobs we quote for you. We break down each step with both labour and materials cost so you can see exactly what you are paying for.</p>
    <p>Feel free to get in touch and we can talk through what you are looking to achieve.</p>
  </div>

  <section class="tile shaded" style="left:124px">
    <div class="icon"><div class="icon-placeholder" role="img" aria-label="Illustration of a case study document with a speech bubble and magnifier"></div></div>
    <h3>Case Studies and<br>Testimonials</h3>
    <p>Ut wisi enim ad minim veniam, quis nostrud exerci tation ullamcorper suscipit lobortis nisl ut aliquip ex ea commodo consequat.</p>
    <a href="#">Read More</a>
  </section>

  <section class="tile" style="left:348px">
    <div class="icon"><svg width="46" height="50" viewBox="0 0 46 50"><path d="M8 2h24l10 10v36H8z" fill="#fff" stroke="var(--brand)" stroke-width="2.5"/><path d="M32 2v10h10" fill="none" stroke="var(--brand)" stroke-width="2.5"/><path d="M18 24h18M18 30h18M18 36h14" stroke="var(--brand)" stroke-width="2"/><path d="M2 36l5 8 7-14" fill="none" stroke="#333" stroke-width="3"/></svg></div>
    <h3>Contact Us For A<br>Free Quote</h3>
    <p>Ut wisi enim ad minim veniam, quis nostrud exerci tation ullamcorper suscipit lobortis nisl ut aliquip ex ea commodo consequat.</p>
    <a href="#">Contact Us</a>
  </section>

  <section class="tile shaded" style="left:572px">
    <div class="icon"><svg width="66" height="50" viewBox="0 0 66 50" role="img" aria-label="Membership badges of Keystone Pact QLT and QLT"><rect x="2" y="2" width="28" height="46" fill="var(--badge-red)"/><rect x="36" y="2" width="28" height="46" fill="var(--badge-red)"/></svg></div>
    <h3>Certifications and Professional<br>Memberships</h3>
    <p>Ut wisi enim ad minim veniam, quis nostrud exerci tation ullamcorper suscipit lobortis nisl ut aliquip ex ea commodo consequat.</p>
    <a href="#">Know More</a>
  </section>

  <footer class="footer" role="img" aria-label="Photo of a row of new stone-clad detached houses at dusk">
    <div class="footer-name">R.T.Harlow Construction Ltd</div>
    <div class="contact-item addr">
      <span class="badge"><svg width="12" height="15" viewBox="0 0 12 16"><path d="M6 0a6 6 0 0 1 6 6c0 4-6 10-6 10S0 10 0 6a6 6 0 0 1 6-6z" fill="#fff"/><circle cx="6" cy="6" r="2.2" fill="var(--brand)"/></svg></span>
      <span>Street Name, City Name<br>State Zipcode</span>
    </div>
    <div class="contact-item call">
      <span class="badge"><svg width="14" height="14" viewBox="0 0 24 24"><path fill="#fff" d="M6.6 10.8a15.1 15.1 0 0 0 6.6 6.6l2.2-2.2c.3-.3.7-.4 1-.2 1.1.4 2.3.6 3.6.6.6 0 1 .4 1 1V20c0 .6-.4 1-1 1C10.6 21 3 13.4 3 4c0-.6.4-1 1-1h3.5c.6 0 1 .4 1 1 0 1.3.2 2.5.6 3.6.1.3 0 .7-.2 1z"/></svg></span>
      <span>Call Us On<br>123.456.7890</span>
    </div>
    <div class="contact-item mail">
      <span class="badge"><svg width="15" height="12" viewBox="0 0 20 14"><rect x="1" y="1" width="18" height="12" fill="none" stroke="#fff" stroke-width="1.6"/><path d="M1 1l9 7 9-7" fill="none" stroke="#fff" stroke-width="1.6"/></svg></span>
      <span>Email<br>info@rtharlowconstruction.com</span>
    </div>
    <div class="copyright">Copyright ©2018 R.T.Harlow Construction Ltd. All Rights Reserved.</div>
    <div class="social"><span></span><span></span><span></span><span></span></div>
  </footer>
</body>
</html>
```